Resume for higher management position in a mechanical/consultant industries application*

I would like to use this resume for getting a higher position interview possibilities. My skills are multi-cultural negotiation, mechanical industry sales, outsourcing to Asia, ability to manage the agent/reseller system, well team player. multi-language Chinese/English/German specialized. Please make the design, professional, comfortable to read atmosphere.

Target Market(s)

management position, sales related

Font styles to use
Serif
Sans Serif

```html
<!DOCTYPE html>
<html lang="en">
<head>
<meta charset="utf-8">
<title>Wen-Hao Liang – Resume</title>
<link rel="stylesheet" href="https://fonts.googleapis.com/css2?family=Arimo:wght@400&family=Open+Sans:wght@400&display=swap">
<style>
  :root {
    --frame: #29292b;
    --paper: #e7e6eb;
    --ink: #222224;
    --muted: #96969a;
    --bar-track: #c7c7ca;
    --bar-fill: #8e8f92;
    --rule-light: #9a9a9d;
  }
  * { margin: 0; padding: 0; box-sizing: border-box; }
  html, body { width: 862px; height: 1200px; overflow: hidden; background: var(--frame); }
  .page { position: relative; width: 862px; height: 1200px; background: var(--frame); }
  .sheet { position: absolute; left: 29px; top: 36px; width: 806px; height: 1128px; background: var(--paper); }
  .abs { position: absolute; }
  .name {
    left: 0; width: 862px; top: 90px; text-align: center;
    font: 400 32px/40px "Arimo", sans-serif; letter-spacing: 9px; color: var(--ink);
  }
  .side-title {
    font: 400 15px/20px "Open Sans", sans-serif; letter-spacing: 3.6px; color: var(--muted);
  }
  .main-title {
    font: 400 15px/20px "Open Sans", sans-serif; letter-spacing: 3.4px; color: var(--ink);
  }
  .rule-light { height: 2px; background: var(--rule-light); }
  .rule-dark { height: 2px; background: var(--ink); }
  .about {
    left: 94px; top: 252px; width: 160px;
    font: 400 10.5px/18.4px "Open Sans", sans-serif; color: var(--muted);
  }
  .contact-icon { position: absolute; left: 78px; width: 36px; height: 36px; }
  .contact-text {
    position: absolute; right: 638px; width: 140px; text-align: right;
    font: 400 10.5px/16px "Open Sans", sans-serif; color: var(--muted);
  }
  .skill-label {
    position: absolute; left: 75px;
    font: 400 9.5px/14px "Open Sans", sans-serif; letter-spacing: 1.4px; color: var(--muted);
  }
  .skill-bar { position: absolute; left: 75px; width: 133px; height: 10px; background: var(--bar-track); }
  .skill-bar span { display: block; height: 100%; background: var(--bar-fill); }
  .job { position: absolute; color: var(--ink); font-family: "Arimo", sans-serif; }
  .job-company { font-size: 18px; line-height: 24px; letter-spacing: 0.4px; }
  .job-role { font-size: 15px; line-height: 22px; letter-spacing: 0.4px; }
  .job-desc { font-size: 13.6px; line-height: 19.5px; letter-spacing: 0.3px; text-align: justify; margin-top: 3px; }
  .edu-school { position: absolute; left: 297px; font: 400 13px/18px "Arimo", sans-serif; color: var(--ink); }
  .edu-degree { position: absolute; right: 40px; font: 400 10.8px/16px "Arimo", sans-serif; color: var(--ink); }
  .achievements {
    left: 76px; top: 907px; width: 729px;
    font: 400 13.6px/22.2px "Arimo", sans-serif; letter-spacing: 0.3px; color: var(--ink); text-align: justify;
  }
</style>
</head>
<body>
<div class="page">
  <div class="sheet"></div>

  <h1 class="abs name">Wen-Hao Liang</h1>

  <!-- About -->
  <h2 class="abs side-title" style="left:95px;top:201px;">ABOUT ME</h2>
  <div class="abs rule-light" style="left:93px;top:228px;width:145px;"></div>
  <p class="abs about">Coordinate Well With Team To Ensure Maximum Effective-ness of Each Task.<br>Well-Versed and a history of successful Career.</p>

  <svg class="contact-icon" style="top:351px" viewBox="0 0 36 36" aria-hidden="true">
    <circle cx="18" cy="18" r="17" fill="none" stroke="#8e8f92" stroke-width="1.6"/>
    <circle cx="18" cy="13" r="5.5" fill="#8e8f92"/>
    <path d="M8 28 q0-9 10-9 q10 0 10 9z" fill="#8e8f92"/>
  </svg>
  <p class="contact-text" style="top:361px">Wen-Hao Liang</p>

  <svg class="contact-icon" style="top:394px" viewBox="0 0 36 36" aria-hidden="true">
    <circle cx="18" cy="18" r="17" fill="none" stroke="#8e8f92" stroke-width="1.6"/>
    <rect x="12.5" y="8" width="11" height="20" rx="2" fill="#8e8f92"/>
    <rect x="14" y="10.5" width="8" height="13" fill="#e7e6eb"/>
    <circle cx="18" cy="25.8" r="0.9" fill="#e7e6eb"/>
  </svg>
  <p class="contact-text" style="top:404px">+123456789</p>

  <svg class="contact-icon" style="top:436px" viewBox="0 0 36 36" aria-hidden="true">
    <circle cx="18" cy="18" r="17" fill="none" stroke="#8e8f92" stroke-width="1.6"/>
    <rect x="8.5" y="11.5" width="19" height="13" fill="#8e8f92"/>
    <path d="M8.5 11.5 L18 19 L27.5 11.5" fill="none" stroke="#e7e6eb" stroke-width="1.2"/>
    <path d="M8.5 24.5 L15 17.5 M27.5 24.5 L21 17.5" fill="none" stroke="#e7e6eb" stroke-width="0.9"/>
  </svg>
  <p class="contact-text" style="top:446px">XXXXX@mailhub.com</p>

  <svg class="contact-icon" style="top:479px" viewBox="0 0 36 36" aria-hidden="true">
    <circle cx="18" cy="18" r="17" fill="none" stroke="#8e8f92" stroke-width="1.6"/>
    <path d="M18 29 C13 22 11 18.5 11 15 a7 7 0 0 1 14 0 c0 3.5-2 7-7 14z" fill="#8e8f92"/>
    <circle cx="18" cy="15" r="2.8" fill="#e7e6eb"/>
  </svg>
  <p class="contact-text" style="top:489px">xxxxxxxx, Germany</p>

  <!-- Skills -->
  <h2 class="abs side-title" style="left:78px;top:523px;">SKILLS</h2>
  <div class="abs rule-light" style="left:76px;top:550px;width:145px;"></div>

  <p class="skill-label" style="top:577px">Project Management</p>
  <div class="skill-bar" style="top:599px"><span style="width:90%"></span></div>
  <p class="skill-label" style="top:634px">Team Work</p>
  <div class="skill-bar" style="top:656px"><span style="width:81%"></span></div>
  <p class="skill-label" style="top:691px">LeaderShip Skills</p>
  <div class="skill-bar" style="top:713px"><span style="width:94%"></span></div>
  <p class="skill-label" style="top:747px">Public Speaking</p>
  <div class="skill-bar" style="top:769px"><span style="width:81%"></span></div>
  <p class="skill-label" style="top:798px">Detail-Oriented</p>
  <div class="skill-bar" style="top:820px"><span style="width:69%"></span></div>

  <!-- Work experience -->
  <h2 class="abs main-title" style="left:300px;top:201px;">WORK EXPERIENCE</h2>
  <div class="abs rule-dark" style="left:297px;top:228px;width:525px;"></div>

  <div class="job" style="left:300px;top:251px;width:522px;">
    <h3 class="job-company">ASIAXXXXXXXXX</h3>
    <p class="job-role">SALES MANAGER&nbsp; 2018 - Now</p>
    <p class="job-desc">Currently, leading 3 major dealers in Taiwan, Mainland China, South Korea and Japan with more than 20 salesmen team. Kestler provides rotary tables, trunnions and 2 axis rotary tilt units shall have the best possible technical characteristics in the smallest possible space, is the principle model for our dividing heads -engineering -manufacturing -and assembly.</p>
  </div>

  <div class="job" style="left:283px;top:408px;width:522px;">
    <h3 class="job-company">LINDQVIST PRECISION MACHINERY COMPANY</h3>
    <p class="job-role">DIRECTOR OF MANUFACTURING, 2012-2017</p>
    <p class="job-desc">Using CNC turn/mill machine to manufacture any mechanical components as customers want. Also providing great total solutions for our clients. Photos shown in my ProLink profile are my products which are made by CNC turn-milling dual spindles machines(trophy is programmed by CAM).</p>
  </div>

  <div class="job" style="left:283px;top:545px;width:522px;">
    <h3 class="job-company">BRIGHTWAY IMPORT MANNHEIM GERMANY</h3>
    <p class="job-role">MARKETING ANALYST, 2012</p>
    <p class="job-desc">Help Brightway Import to build their sales/marketing strategy for the new launched product “Slick-Seal” in central Europe.</p>
  </div>

  <div class="job" style="left:283px;top:645px;width:522px;">
    <h3 class="job-company">VALLECEMENTI GROUP BERGAMO ITALTY</h3>
    <p class="job-role">EXTERNAL CONSULTANT, 2011-2012</p>
    <p class="job-desc" style="line-height:22px;text-align:left;margin-top:0;">To improve the Orbita solution(ERP system) of Vallecementi with re-organized procurement process and new standardized KPIs.</p>
  </div>

  <!-- Education -->
  <h2 class="abs main-title" style="left:300px;top:760px;">EDUCATION</h2>
  <div class="abs rule-dark" style="left:297px;top:788px;width:528px;"></div>
  <p class="edu-school" style="top:813px">POLITECNICO DI ALVARENA ITALY</p>
  <p class="edu-degree" style="top:815px">MASTER OF BUSINESS ADMNISTRATION (MBA)</p>
  <p class="edu-school" style="top:846px">TAI-MING CHRISTIAN UNIVERSITY</p>
  <p class="edu-degree" style="top:848px">BACHELOR OF CHEMICAL ENGINEERING</p>

  <!-- Achievements -->
  <h2 class="abs main-title" style="left:78px;top:865px;">ACHIEVEMENTS</h2>
  <div class="abs rule-dark" style="left:76px;top:893px;width:729px;"></div>
  <p class="abs achievements">Mandarin Chinese/ German/ English speaker, real machining experiences, OEM skills, trade skill, global sourcing.Currently, I am a “Sales manager Asia” of a top German rotary table company. I am in charge of four countries Japan, China, South Korea and Taiwan with 3 agents, more than 20 salemen team.<br>As a director of manufacuturing, I have more than 5 years professional experiences in manufacturing metal components by different CNC-machines. I am capable of coding CNC G,M-code, designing the wor-king path of different parts and managing the whole process.<br>I have well-understanding of mechanical outsourcing ecosystem in Taiwan. With deep knowledge of outsourcing metal components to different suppliers in Taiwan.Familiar with coordinating with different industrial processes in order to build the final products. (Black oxidizing, Different anodizing, Chemical polishing, Manganese phosphate coating, Heat treatment, and Different grinding methods) Especially love to build prototype in order to get a high profitable potential products. (from zero to one)</p>
</div>
</body>
</html>
```